Produktbroschüre
Zielgruppe
Einzelhändler im Einrichtungs-, Geschenk- und Blumanfachhandel, Dekorateure, Innenarchitekten,
Aufgabenstellung
Ich bin Existenzgründer und brauche eine ansprechende Produktbroschüre für Inneneinrichtungsdeko und Accessoires.
Die Artikel wechseln öfter und ich möchte in der Lage sein Bilder und Texte einfach auszutauschen. Über die zeit, wird das Sortiment erwetert, die Broschüre sollte einfach mitwachsen können.
Momentan behelfe ich mir mit Scribus und Gimp für Windows, bin aber kein Experte.
Als Anhang meine momentane, selbst gebaute Broschüre.

```html
<!DOCTYPE html>
<html lang="de">
<head>
<meta charset="utf-8">
<title>sorel bunt – Produktbroschüre</title>
<link rel="stylesheet" href="https://fonts.googleapis.com/css2?family=Fira+Sans:wght@400;600&display=swap">
<style>
  :root {
    --backdrop: #e9e6e1;
    --paper: #ffffff;
    --orange: #f08a24;
    --ink-dark: #3a2412;
    --ink-light: #ffffff;
  }
  * { margin: 0; padding: 0; box-sizing: border-box; }
  html, body {
    width: 1200px; height: 1200px; overflow: hidden;
    background: var(--backdrop);
    font-family: "Fira Sans", sans-serif;
  }
  .spread {
    position: absolute;
    left: 40px; top: 270px;
    width: 1120px; height: 660px;
    background: var(--paper);
    display: flex;
    box-shadow: 0 6px 24px rgba(0,0,0,.12);
  }
  .page {
    position: relative;
    width: 560px; height: 660px;
  }
  .page + .page { border-left: 1px solid #eeeae4; }
  .page-shape { position: absolute; inset: 0; }
  .page-shape path { fill: var(--orange); }
  .contact-line {
    position: absolute;
    left: 30px; top: 404px;
    font-size: 13px; line-height: 1.45;
    color: var(--ink-light);
    white-space: nowrap;
  }
  .contact-line .brand-name { font-weight: 600; }
  .tagline {
    position: absolute;
    left: 50px; top: 408px;
    font-size: 13px;
    color: var(--ink-light);
    white-space: nowrap;
  }
  .tagline .brand-name { font-weight: 600; }
  .tagline .range {
    margin-left: 10px;
    font-size: 17px; font-weight: 600;
    color: var(--ink-dark);
  }
  .plus {
    position: absolute;
    right: 42px; top: 440px;
    font-size: 30px; font-weight: 600; line-height: 1;
    color: var(--ink-dark);
  }
</style>
</head>
<body>
  <main class="spread">
    <section class="page page-contact">
      <svg class="page-shape" viewBox="0 0 560 660" aria-hidden="true">
        <path d="M50 30 H510 Q530 30 530 50 V480 Q530 500 510 500 H200 Q180 500 175 485 L168 470 Q163 458 150 458 H50 Q30 458 30 438 V50 Q30 30 50 30 Z"/>
        <path d="M50 478 H145 Q160 478 165 490 L172 508 Q177 520 195 520 H510 Q530 520 530 540 V610 Q530 630 510 630 H50 Q30 630 30 610 V498 Q30 478 50 478 Z"/>
      </svg>
      <p class="contact-line"><span class="brand-name">sorel bunt</span> | Jonas K. Albers | Lindenhofweg 4 | 85110 Kirchbergen<br>Tel.: +49 (0)176 55 204118 | info@sorel-bunt.com | www.sorel-bunt.com</p>
      <span class="plus">+</span>
    </section>
    <section class="page page-cover">
      <svg class="page-shape" viewBox="0 0 560 660" aria-hidden="true">
        <path d="M50 30 H510 Q530 30 530 50 V480 Q530 500 510 500 H200 Q180 500 175 485 L168 470 Q163 458 150 458 H50 Q30 458 30 438 V50 Q30 30 50 30 Z"/>
        <path d="M50 478 H145 Q160 478 165 490 L172 508 Q177 520 195 520 H510 Q530 520 530 540 V610 Q530 630 510 630 H50 Q30 630 30 610 V498 Q30 478 50 478 Z"/>
      </svg>
      <p class="tagline"><span class="brand-name">sorel bunt</span><span class="range">Wohn- und Tischkultur | Lifestyle | Gartendeko</span></p>
      <span class="plus">+</span>
    </section>
  </main>
</body>
</html>
```